Business Card Design Project

We need a business card design for a company based in San Francisco called PlanGlide. PlanGlide makes customized academic planners for high schools and middle schools. Currently we sell directly to the schools who either re-sell or give the planners to their students. The planners are designed to help students stay organized and manage their time. The books are unique in that they are made individually for each school and include the school's events, student artwork and most importantly the daily class schedule in each week. This helps the student to understand what classes they have each day and what homework they need to do each night.

Currently the product is B:B; however, we are exploring ways in which to make this a B:C. Please review website at www.planglide.net

The final design should communicate time management and organization.

Card should be one-sided

Information for the business card should include

Dorothy Kellner Voss
Founder
dorothy@planglide.net
415-836-1752

Target Market(s)

High school and middle school administrators

Industry/Entity Type

School

Requirements
Must have
• One sided design
Nice to have
• I'm open to new interpretations of the logo as well as color usage. I'm also open to changing the font of the logo type.
Should not have
• Please use a san serif font.

```html
<!DOCTYPE html>
<html lang="en">
<head>
<meta charset="utf-8">
<title>PlanGlide — Business Card</title>
<link rel="stylesheet" href="https://fonts.googleapis.com/css2?family=Fira+Sans:wght@400;600&family=Arimo:wght@400;700&display=swap">
<style>
  :root {
    --page-bg: #ecebe7;
    --card-bg: #f4f4f2;
    --ink: #1b1b1b;
    --accent-red: #c8102e;
    --ribbon-blue: #5169a9;
    --ribbon-red: #b3453f;
    --ribbon-green: #4ba646;
    --footer-olive: #a49e5b;
    --ribbon-text: #ffffff;
  }
  * { box-sizing: border-box; margin: 0; padding: 0; }
  html, body {
    width: 1200px;
    height: 900px;
    overflow: hidden;
    background: var(--page-bg);
  }
  .canvas {
    position: relative;
    width: 1200px;
    height: 900px;
  }
  .business-card {
    position: absolute;
    left: 150px;
    top: 210px;
    width: 900px;
    height: 480px;
    background: var(--card-bg);
    box-shadow: 0 6px 22px rgba(0,0,0,0.18);
    overflow: hidden;
  }
  .brand {
    position: absolute;
    left: 66px;
    top: 28px;
  }
  .brand-name {
    display: flex;
    align-items: center;
    gap: 12px;
    font-family: "Fira Sans", sans-serif;
    font-weight: 600;
    font-size: 46px;
    line-height: 1;
    color: var(--ink);
    letter-spacing: -0.5px;
  }
  .brand-mark {
    width: 14px;
    height: 14px;
    background: var(--accent-red);
  }
  .brand-tagline {
    margin-top: 10px;
    font-family: "Fira Sans", sans-serif;
    font-weight: 400;
    font-size: 23px;
    color: var(--accent-red);
  }
  .check-list {
    position: absolute;
    left: 64px;
    top: 168px;
    display: flex;
    flex-direction: column;
    gap: 54px;
  }
  .check-icon { width: 34px; height: 32px; display: block; }
  .ribbon {
    position: absolute;
    right: 0;
    height: 76px;
    display: flex;
    flex-direction: column;
    justify-content: center;
    align-items: flex-end;
    padding-right: 54px;
    clip-path: polygon(0 0, 100% 0, 100% 100%, 0 100%, 48px 50%);
    font-family: "Arimo", sans-serif;
    color: var(--ribbon-text);
    text-transform: uppercase;
    line-height: 1.3;
  }
  .ribbon-identity { top: 163px; width: 471px; background: var(--ribbon-blue); font-size: 22px; }
  .ribbon-email    { top: 245px; width: 563px; background: var(--ribbon-red);  font-size: 22px; }
  .ribbon-contact  { top: 326px; width: 663px; background: var(--ribbon-green); }
  .contact-phone { font-size: 26px; font-weight: 700; }
  .contact-web   { font-size: 21px; font-weight: 700; }
  .card-footer {
    position: absolute;
    left: 0;
    bottom: 0;
    width: 100%;
    height: 44px;
    background: var(--footer-olive);
  }
</style>
</head>
<body>
<div class="canvas">
  <article class="business-card">
    <header class="brand">
      <div class="brand-name">PlanGlide <span class="brand-mark"></span></div>
      <p class="brand-tagline">Customized Academic Planners</p>
    </header>

    <div class="check-list" aria-hidden="true">
      <svg class="check-icon" viewBox="0 0 34 32"><rect x="2" y="9" width="20" height="20" fill="none" stroke="#1b1b1b" stroke-width="2.5"/><path d="M6 18 L12 25 L30 2" fill="none" stroke="#c8102e" stroke-width="3.5" stroke-linecap="round" stroke-linejoin="round"/></svg>
      <svg class="check-icon" viewBox="0 0 34 32"><rect x="2" y="9" width="20" height="20" fill="none" stroke="#1b1b1b" stroke-width="2.5"/><path d="M6 18 L12 25 L30 2" fill="none" stroke="#c8102e" stroke-width="3.5" stroke-linecap="round" stroke-linejoin="round"/></svg>
      <svg class="check-icon" viewBox="0 0 34 32"><rect x="2" y="9" width="20" height="20" fill="none" stroke="#1b1b1b" stroke-width="2.5"/><path d="M6 18 L12 25 L30 2" fill="none" stroke="#c8102e" stroke-width="3.5" stroke-linecap="round" stroke-linejoin="round"/></svg>
    </div>

    <div class="ribbon ribbon-identity">
      <span class="contact-name">Dorothy Kellner Voss</span>
      <span class="contact-title">Founder</span>
    </div>
    <div class="ribbon ribbon-email">
      <span class="contact-email">dorothy@planglide.net</span>
    </div>
    <div class="ribbon ribbon-contact">
      <span class="contact-phone">415-836-1752</span>
      <span class="contact-web">www.planglide.net</span>
    </div>

    <div class="card-footer"></div>
  </article>
</div>
</body>
</html>
```